Postcard Mail Out - Wendell

We are a real estate company. We need a post card to mail out to potential clients to try and sale their land. We will attached a couple of post cards that we like but we do not want to copy them completely. We do need to put the Fair Dwelling Access and the Homevest logos with a disclosure saying not intended to solicit currently listed properties. The image below is what we had started working on. We would like to include something about farm land, timber, maybe a pond, something along those lines. The PDF Files attached are a flyer that was mailed out by another company that we do not want to copy completely. Attached also will be our company's Logo.

Requirements
Must have
• We do need to put the Fair Dwelling Access and the Homevest logos with a disclosure saying not intended to solicit currently listed properties.<br/><br/>At Sol Brantham Summit Realty, we are blessed to have one of the very best Rural Land Specialists available. Wendell has years of experience promoting and selling rural land properties. Wendell has earned the trust of many landowners, as he is so PASSIONATE in all regards to rural land, farms and ranches. He has made a wide range of landowners very happy throughout his years in Real Estate. Call him today and show him your property, and he will provide you with a free analysis and strategy to maximize the return on your property.
Nice to have
• A picture of Wendell has been added to use on the back of the post card with his phone and number. It would be nice to have a east Texas scenery picture behind him instead of an office.<br/><br/>Please include front and back of post card in your submission.
Should not have
• Should not have Marcus Vell's information on the postcard. That post card was just to show what we was wanting. The agent we want listed is Wendell Harbin and his phone number is (555)214-3098.

```html
<!DOCTYPE html>
<html lang="en">
<head>
<meta charset="utf-8">
<title>Rural Land Postcard – Sol Brantham Summit Realty</title>
<link rel="stylesheet" href="https://fonts.googleapis.com/css2?family=Vollkorn:wght@400;700&family=Roboto+Condensed:wght@400;700&display=swap">
<style>
  :root {
    --page: #ffffff;
    --ink: #1d1d1d;
    --panel-grey: #b7bbba;
    --headline: #ffffff;
    --forest-top: #3f6b2a;
    --forest-mid: #5c8a3a;
    --trunk: #4a5a44;
    --grass-light: #7e9a2e;
    --grass-deep: #5f7a22;
    --grass-gold: #a68a3a;
    --reed-dark: #2f3324;
    --water-light: #6a9ae0;
    --water-deep: #3f7ad6;
    --shadow: rgba(0,0,0,0.28);
  }
  * { margin: 0; padding: 0; box-sizing: border-box; }
  html, body {
    width: 1200px; height: 1200px; overflow: hidden;
    background: var(--page);
  }
  .card {
    position: absolute;
    left: 213px; width: 781px; height: 521px;
    box-shadow: 2px 4px 6px var(--shadow);
    overflow: hidden;
  }
  .card--front { top: 40px; }
  .card--back { top: 596px; background: var(--page); }

  /* Front */
  .scene { position: absolute; left: 0; width: 100%; }
  .scene--forest {
    top: 0; height: 174px;
    background: linear-gradient(90deg, var(--forest-top), var(--forest-mid) 30%, var(--trunk) 50%, var(--forest-mid) 70%, var(--forest-top));
  }
  .scene--meadow {
    top: 174px; height: 174px;
    background: linear-gradient(180deg, var(--grass-light), var(--grass-deep) 60%, var(--grass-gold));
  }
  .scene--pond {
    top: 348px; height: 173px;
    background: linear-gradient(180deg, var(--reed-dark) 0%, #33424c 45%, #4f7fbf 75%, var(--water-deep));
  }
  .headline {
    position: absolute; left: 0; top: 212px; width: 100%;
    text-align: center;
    font-family: "Vollkorn", Georgia, serif;
    font-weight: 400; font-size: 35px; line-height: 45px;
    color: var(--headline);
    letter-spacing: 0.5px;
  }
  .specialist {
    position: absolute; left: 40px; top: 362px; width: 701px;
    text-align: center;
    font-family: "Vollkorn", Georgia, serif;
    color: var(--headline);
  }
  .specialist-name {
    font-size: 18px; line-height: 24px; font-weight: 700;
    margin-bottom: 6px;
  }
  .specialist-copy { font-size: 13px; line-height: 17.5px; }

  /* Back */
  .message {
    position: absolute; left: 24px; top: 48px; width: 470px;
    font-family: "Vollkorn", Georgia, serif;
    font-size: 17px; line-height: 21.7px;
    color: var(--ink);
  }
  .message p { margin-bottom: 21.7px; }
  .message strong { font-weight: 700; }
  .offer-heading { margin-bottom: 0 !important; }
  .offer-list { list-style: none; }

  .contact-panel {
    position: absolute; left: 521px; top: 0; width: 260px; height: 100%;
    background: var(--panel-grey);
    color: var(--ink);
  }
  .brand {
    position: absolute; left: 38px; top: 66px; width: 200px;
    display: flex; align-items: center; gap: 9px;
    font-family: "Vollkorn", Georgia, serif;
    font-weight: 700; font-size: 17px; line-height: 20px;
  }
  .brand-mark { width: 16px; height: 16px; background: var(--ink); flex: none; }
  .phone {
    position: absolute; left: 0; top: 129px; width: 100%;
    text-align: center;
    font-family: "Roboto Condensed", "Arial Narrow", sans-serif;
    font-weight: 700; font-size: 31px; line-height: 36px;
  }
  .website {
    position: absolute; left: 0; top: 170px; width: 100%;
    text-align: center;
    font-family: "Roboto Condensed", "Arial Narrow", sans-serif;
    font-size: 17px; line-height: 20px;
  }
  .address {
    position: absolute; left: 38px; top: 229px;
    font-family: "Vollkorn", Georgia, serif; font-style: normal;
    font-size: 14.4px; line-height: 18.8px;
  }
  .agent { font-weight: 700; }
  .badges {
    position: absolute; left: 36px; top: 368px;
    display: flex; gap: 18px; align-items: flex-start;
  }
  .badge {
    display: flex; flex-direction: column; align-items: center; gap: 4px;
    font-family: "Roboto Condensed", "Arial Narrow", sans-serif;
    text-align: center;
  }
  .badge--fair { font-size: 10px; line-height: 10px; text-transform: uppercase; width: 91px; }
  .badge--homevest { font-size: 14px; line-height: 16px; font-weight: 700; text-transform: uppercase; letter-spacing: 0.5px; }
  .badge-shape { display: block; }
  .disclosure {
    position: absolute; left: 24px; top: 480px; width: 212px;
    font-family: "Vollkorn", Georgia, serif;
    font-size: 9.5px; line-height: 12px; text-align: center;
  }
</style>
</head>
<body>

<section class="card card--front">
  <div class="scene scene--forest" role="img" aria-label="Photograph of a sunlit stand of hardwood timber"></div>
  <div class="scene scene--meadow" role="img" aria-label="Photograph of a green grassy pasture"></div>
  <div class="scene scene--pond" role="img" aria-label="Photograph of a blue pond with reeds reflected along the bank"></div>
  <h1 class="headline">LAND FOR SALE?<br>SPECIALIZING IN RURAL LAND SALES</h1>
  <div class="specialist">
    <p class="specialist-name">Wendell Harbin, Rural Land Specialist &nbsp;·&nbsp; (555)214-3098</p>
    <p class="specialist-copy">At Sol Brantham Summit Realty, we are blessed to have one of the very best Rural Land Specialists available. Wendell has years of experience promoting and selling rural land properties. Wendell has earned the trust of many landowners, as he is so PASSIONATE in all regards to rural land, farms and ranches. He has made a wide range of landowners very happy throughout his years in Real Estate. Call him today and show him your property, and he will provide you with a free analysis and strategy to maximize the return on your property.</p>
  </div>
</section>

<section class="card card--back">
  <div class="message">
    <p><strong>Looking for a place to call home?</strong> Use Quick Search or Map Search in summitlandrealty.com to browse an up-to-date database list of all available properties in the area, or use our Dream Home Finder form and we will conduct a personalized search for you!</p>
    <p><strong>If you're planning to sell your home in the next few months</strong>, nothing is more important than knowing a fair asking price. We would love to help you with a FREE Market Analysis. We will use comparable sold listings to help you determine the accurate market value of your home.</p>
    <p class="offer-heading"><strong>We offer:</strong></p>
    <ul class="offer-list">
      <li>Single Family Home</li>
      <li>Farm</li>
      <li>Manufactured Home</li>
      <li>Residential Lots &amp; Land</li>
      <li>Commercial</li>
      <li>Multi Family Home</li>
    </ul>
  </div>

  <aside class="contact-panel">
    <div class="brand"><span class="brand-mark"></span><span>Sol Brantham Summit Realty</span></div>
    <div class="phone">(555)214-3098</div>
    <div class="website">summitlandrealty.com</div>
    <address class="address">
      <span class="agent">Wendell Harbin</span><br>
      Sol Brantham Summit Realty<br>
      418 Cedar Row<br>
      Pine Hollow, TX 75000<br>
      Office: 555-410-7286<br>
      Fax: 555-410-7290
    </address>
    <div class="badges">
      <div class="badge badge--fair">
        <svg class="badge-shape" width="91" height="78" viewBox="0 0 91 78" aria-hidden="true"><rect x="6" y="0" width="79" height="78" fill="#1d1d1d"/></svg>
        <span>Fair Dwelling Access</span>
      </div>
      <div class="badge badge--homevest">
        <svg class="badge-shape" width="74" height="74" viewBox="0 0 74 74" aria-hidden="true"><rect x="0" y="0" width="74" height="74" fill="#1d1d1d"/></svg>
        <span>Homevest</span>
      </div>
    </div>
    <p class="disclosure">Not intended to solicit properties currently listed with another broker.</p>
  </aside>
</section>

</body>
</html>
```